New ecommerce website needed for Epoxy Retailer

We need a new shopify website designed and built for our epoxy supply store.
We sell Epoxy, wood, epoxy furniture, supplies and provide classes on how to use epoxy.
We are looking for a website with a home page and 7 primary navigation links at the top. Some of these links should have a drop down menu with the below listed pages linked to them...
Sub Pages:
- Brindle Epoxy
- Epoxy
- Pigments
- Marten Oil
- Molds
- Silicone
- HDPE
- Wood
- Live Edge
- Ovals & Rounds
- Pre-cut
- Charcuterie Wood
- Custom Milling
- Wholesale
- Supplies
- Furniture
-Education
- In person workshops
- My courses (are we able to have a login section for customers to see their purchases?)
- About Us

```html
<!DOCTYPE html>
<html lang="en">
<head>
<meta charset="utf-8">
<title>Timberpour — Epoxy Supply Store</title>
<link href="https://fonts.googleapis.com/css2?family=Bebas+Neue&family=Poppins:wght@400;500;600&display=swap" rel="stylesheet">
<style>
:root{
  --ink:#111111;
  --dark:#232323;
  --band:#2a2a2a;
  --grey:#6d6d6d;
  --light:#f2f2f2;
  --peach:#f7e7db;
  --line:#dcdcdc;
  --star:#e8a33c;
  --btn-grey:#9b9b9b;
  --white:#ffffff;
}
*{margin:0;padding:0;box-sizing:border-box}
html,body{width:1200px;height:4852px;overflow:hidden;background:var(--white)}
body{font-family:"Poppins",sans-serif;color:var(--ink);position:relative;font-size:14px}
.display{font-family:"Bebas Neue",sans-serif;font-weight:400;letter-spacing:.5px}
.abs{position:absolute}

/* header */
.brand{left:88px;top:40px;display:flex;align-items:center;gap:10px}
.brand-mark{width:40px;height:40px;border-radius:50%;background:var(--ink)}
.brand-name{font-family:"Bebas Neue",sans-serif;font-size:30px;color:var(--ink)}
.nav{right:88px;top:30px;display:flex;align-items:center;gap:22px;font-size:11px;font-weight:600;letter-spacing:.3px}
.nav a{color:var(--ink);text-decoration:none}
.nav .login{border:1.5px solid var(--ink);padding:10px 20px}

/* hero */
.hero-img{left:540px;top:80px;width:660px;height:660px;background:linear-gradient(135deg,#3e6f86 0%,#c79a63 45%,#a8743f 65%,#2f8fb8 100%)}
.hero-shadow{left:560px;top:700px;width:620px;height:60px;box-shadow:0 24px 40px rgba(0,0,0,.22);z-index:-1}
.hero-title{left:88px;top:300px;font-size:84px;line-height:.98;width:440px}
.hero-copy{left:88px;top:480px;width:380px;font-size:15px;line-height:1.45;color:#333}
.btn-dark{background:var(--ink);color:var(--white);font-size:11px;font-weight:600;display:inline-flex;align-items:center;gap:14px;padding:14px 22px}
.hero-btn{left:88px;top:548px}

/* promo */
.promo-left{left:88px;top:848px;width:500px;height:424px;background:var(--light)}
.promo-left .art{position:absolute;right:24px;top:60px;width:230px;height:300px;background:radial-gradient(circle at 50% 35%,#1f5d9c 0,#6a8fb3 35%,#d8b489 60%,#f2f2f2 75%)}
.promo-title{position:absolute;left:40px;top:160px;font-size:52px;line-height:.95}
.btn-sm{position:absolute;background:var(--ink);color:var(--white);font-size:9px;font-weight:600;padding:8px 14px}
.promo-left .btn-sm{left:40px;top:280px}
.promo-wood{left:600px;top:848px;width:512px;height:204px;background:var(--peach)}
.promo-wood .art{position:absolute;right:0;top:0;width:250px;height:204px;background:linear-gradient(120deg,#c08a55,#7a4a24 60%,#d9b585)}
.promo-wood .promo-title{left:40px;top:56px;font-size:62px}
.promo-wood .sub{position:absolute;left:42px;top:116px;font-size:9px;font-weight:600}
.promo-epoxy{left:600px;top:1068px;width:512px;height:204px;background:linear-gradient(110deg,#6b4a2e,#2f86b5 45%,#8fc3df 70%,#5a3a22)}
.promo-epoxy span{position:absolute;left:0;right:0;top:70px;text-align:center;font-size:58px;color:var(--white)}

/* category */
.category{left:0;top:1388px;width:1200px;height:488px;background:linear-gradient(180deg,#1e1e1e,#343434 50%,#1f1f1f)}
.section-title{font-size:40px;text-align:center;width:100%}
.category .section-title{position:absolute;top:110px;color:var(--white)}
.cat-row{position:absolute;left:84px;top:196px;width:1032px;display:flex;justify-content:space-between}
.cat{width:132px;height:132px;border-radius:50%;border:4px dashed #d8d8d8;display:flex;flex-direction:column;align-items:center;justify-content:center;gap:10px;color:var(--white);font-size:10px;font-weight:600;text-transform:uppercase;background:var(--dark)}
.cat svg{width:40px;height:40px;stroke:var(--white);fill:none;stroke-width:2.4}
.dots{position:absolute;display:flex;gap:6px;left:0;right:0;justify-content:center}
.dots i{width:7px;height:7px;border-radius:50%;background:#888}
.dots i.on{background:var(--white)}
.category .dots{top:420px}

/* products */
.products-title{top:1980px}
.product-row{left:88px;top:2048px;width:1024px;display:flex;justify-content:space-between}
.product{width:240px;height:320px;background:var(--white);box-shadow:0 6px 24px rgba(0,0,0,.12);text-align:center;padding-top:24px}
.product .art{width:150px;height:170px;margin:0 auto 16px}
.product h3{font-size:13px;font-weight:600;font-family:"Bebas Neue",sans-serif;font-size:18px;letter-spacing:.4px}
.stars{color:var(--star);font-size:13px;letter-spacing:2px;margin:4px 0}
.price{font-size:18px;font-weight:500}
.products-dots{top:2400px}
.products-dots i{background:#bbb}
.products-dots i.on{background:var(--ink)}

/* about / how-to */
.about-img{left:140px;top:2480px;width:380px;height:380px;border-radius:50%;background:radial-gradient(circle,#b58a5c,#6e4a2d 70%,#2a1b10);border:10px dashed var(--ink)}
.text-block h2{font-size:46px;margin-bottom:10px}
.text-block p{font-size:15px;line-height:1.5;color:#333}
.about{left:560px;top:2540px;width:520px}
.btn-line{display:inline-block;margin-top:20px;border:1.5px solid var(--ink);padding:10px 18px;font-size:11px;font-weight:600}
.howto{left:88px;top:2900px;width:560px}
.howto-img{left:660px;top:2860px;width:400px;height:400px;border-radius:50%;background:radial-gradient(circle,#e0a860,#9a5a22 55%,#1b1b1b);border:10px dashed var(--ink)}

/* blog */
.blog-title{top:3336px}
.blog-row{left:128px;top:3408px;width:944px;display:flex;justify-content:space-between}
.post{width:308px;box-shadow:0 6px 22px rgba(0,0,0,.12);background:var(--white)}
.post .art{height:216px}
.post .body{padding:24px 20px 22px}
.post h4{font-size:11px;font-weight:600;margin-bottom:6px}
.post p{font-size:11px;line-height:1.45;color:#555}
.post .more{font-size:9px;font-weight:600;margin-top:8px;display:block}

/* features */
.features{left:200px;top:3860px;width:800px;display:flex;justify-content:space-between}
.feature{width:180px;text-align:center}
.feature svg{width:40px;height:34px;stroke:var(--ink);fill:none;stroke-width:2}
.feature b{display:block;font-size:13px;font-weight:600;margin-top:4px}
.feature span{font-size:11px;color:var(--grey)}

/* forest + footer */
.forest{left:0;top:3980px;width:1200px;height:270px;background:linear-gradient(180deg,rgba(0,0,0,0) 0%,#555 40%,#000 100%)}
.footer{left:0;top:4248px;width:1200px;height:604px;background:#000;color:var(--white)}
.newsletter{position:absolute;left:88px;top:48px}
.newsletter h2{font-size:34px}
.newsletter p{font-size:12px;color:#ccc;width:380px;line-height:1.5}
.signup{position:absolute;left:640px;top:72px;display:flex}
.signup .field{width:320px;height:52px;background:var(--white);color:#777;font-size:12px;padding:17px 20px}
.signup .go{width:152px;height:52px;background:var(--btn-grey);font-size:13px;font-weight:600;text-align:center;padding-top:16px}
.foot-brand{position:absolute;left:120px;top:252px;display:flex;align-items:center;gap:12px}
.foot-brand .brand-mark{background:var(--white);width:52px;height:52px}
.foot-brand .brand-name{color:var(--white);font-size:34px}
.col{position:absolute;top:232px;font-size:12px;line-height:1.9}
.col h5{font-size:13px;font-weight:600;margin-bottom:6px;letter-spacing:.4px}
.col a{color:#e6e6e6;text-decoration:none;display:block}
.social{display:flex;gap:10px;margin-top:4px}
.social i{width:12px;height:12px;border-radius:50%;background:var(--white)}
.copyright{position:absolute;left:0;right:0;top:564px;text-align:center;font-size:12px;color:#ccc}
.to-top{position:absolute;right:30px;top:552px;width:36px;height:36px;border-radius:50%;background:#3a3a3a;display:flex;align-items:center;justify-content:center}
</style>
</head>
<body>

<header>
  <div class="abs brand"><span class="brand-mark"></span><span class="brand-name">Timberpour</span></div>
  <nav class="abs nav">
    <svg width="14" height="14" viewBox="0 0 24 24"><path d="M3 11 12 3l9 8v10h-6v-6H9v6H3z" fill="#111"/></svg>
    <a href="#">PRODUCTS</a><a href="#">CATEGORIES</a><a href="#">ABOUT US</a><a href="#">BLOG</a><a href="#">EPOXY TRAINING</a><a href="#">CONTACT US</a><a class="login" href="#">LOGIN</a>
  </nav>
</header>

<section class="hero">
  <div class="abs hero-shadow"></div>
  <div class="abs hero-img" role="img" aria-label="Live edge wood dining table with blue epoxy river and teal chairs"></div>
  <h1 class="abs hero-title display">Our Epoxy Supply Store</h1>
  <p class="abs hero-copy">We sell Epoxy, wood, epoxy furniture, supplies and provide classes on how to use epoxy.</p>
  <a class="abs hero-btn btn-dark">OUR PRODUCTS <span>→</span></a>
</section>

<section class="promos">
  <div class="abs promo-left">
    <h2 class="promo-title display">Epoxy<br>Furniture</h2>
    <span class="btn-sm">SHOP NOW</span>
    <div class="art" role="img" aria-label="Round wooden side table with blue epoxy top"></div>
  </div>
  <div class="abs promo-wood">
    <h2 class="promo-title display">Wood</h2>
    <span class="sub">SHOP NOW</span>
    <div class="art" role="img" aria-label="Stack of cut wooden logs"></div>
  </div>
  <div class="abs promo-epoxy" role="img" aria-label="Close-up of blue epoxy poured over wood"><span class="display">We Sell Epoxy</span></div>
</section>

<section class="abs category">
  <h2 class="section-title display">Category</h2>
  <div class="cat-row">
    <div class="cat"><svg viewBox="0 0 40 40"><path d="M20 4v32M6 12l28 16M34 12 6 28"/></svg>Brindle Epoxy</div>
    <div class="cat"><svg viewBox="0 0 40 40"><path d="M20 5c7 10 11 16 11 21a11 11 0 0 1-22 0c0-5 4-11 11-21z"/></svg>Epoxy</div>
    <div class="cat"><svg viewBox="0 0 40 40"><path d="M15 4h10v8l4 6v18H11V18l4-6z"/></svg>Pigments</div>
    <div class="cat"><svg viewBox="0 0 40 40"><rect x="10" y="10" width="20" height="26" rx="3"/><path d="M15 4h10v6H15z"/></svg>Marten Oil</div>
    <div class="cat"><svg viewBox="0 0 40 40"><rect x="6" y="10" width="28" height="20" rx="2"/><path d="M12 16h16v8H12z"/></svg>Molds</div>
    <div class="cat"><svg viewBox="0 0 40 40"><path d="M8 30 26 12l4 4-18 18H8zM26 12l4-6 4 4-4 6"/></svg>Silicone</div>
  </div>
  <div class="dots"><i class="on"></i><i></i><i></i></div>
</section>

<section class="products">
  <h2 class="abs section-title display products-title">Our Products</h2>
  <div class="abs product-row">
    <article class="product"><div class="art" role="img" aria-label="Two bottles of epoxy resin" style="background:linear-gradient(90deg,#1d2a6b,#3a7fd0)"></div><h3>Products Heading Here</h3><div class="stars">★★★★★</div><div class="price">$54.00</div></article>
    <article class="product"><div class="art" role="img" aria-label="Round wood slices" style="background:linear-gradient(180deg,#e3c291,#a06a38)"></div><h3>Products Heading Here</h3><div class="stars">★★★★★</div><div class="price">$54.00</div></article>
    <article class="product"><div class="art" role="img" aria-label="Wood and epoxy chair" style="background:linear-gradient(180deg,#8b9c9a,#4b3a2a)"></div><h3>Products Heading Here</h3><div class="stars">★★★★★</div><div class="price">$54.00</div></article>
    <article class="product"><div class="art" role="img" aria-label="Large jugs of epoxy resin" style="background:linear-gradient(90deg,#1b2f6e,#2c66b8)"></div><h3>Products Heading Here</h3><div class="stars">★★★★★</div><div class="price">$54.00</div></article>
  </div>
  <div class="abs dots products-dots"><i class="on"></i><i></i><i></i></div>
</section>

<section>
  <div class="abs about-img" role="img" aria-label="Rough wood planks in a workshop"></div>
  <div class="abs about text-block">
    <h2 class="display">About Timberpour</h2>
    <p>Lorem ipsum is simply dummy text of the printing and typesetting industry. Lorem Ipsum has been the industry's standard dummy text ever since the 1500s, when an unknown printer took a galley of type and scrambled it to make a type specimen book. It has survived not only five centuries, but also the leap into.</p>
    <span class="btn-line">READ MORE</span>
  </div>
</section>

<section>
  <div class="abs howto text-block">
    <h2 class="display">How to Use Epoxy</h2>
    <p>Use sandpaper to roughen the surfaces you're going to bond.<br>Prepare the application syringe.<br>Get ready to mix.<br>Retract the plunger.<br>Mix the epoxy resin and hardener quickly.<br>Apply a small amount of glue to the surfaces you're bonding.<br>Carefully remove any excess epoxy.</p>
  </div>
  <div class="abs howto-img" role="img" aria-label="Wood surface with amber epoxy inlay"></div>
</section>

<section>
  <h2 class="abs section-title display blog-title">Latest Blog</h2>
  <div class="abs blog-row">
    <article class="post"><div class="art" role="img" aria-label="Blue epoxy being poured" style="background:linear-gradient(135deg,#0d4f8a,#69b3e0,#c6a06c)"></div><div class="body"><h4>BLOG HEADING HERE</h4><p>Lorem ipsum is simply dummy text of the printing and typesetting industry. Lorem Ipsum has been the industry's.</p><span class="more">READ MORE</span></div></article>
    <article class="post"><div class="art" role="img" aria-label="Roller applying epoxy coat to a floor" style="background:linear-gradient(135deg,#2a7fb0,#e8eef2,#9fb6c4)"></div><div class="body"><h4>BLOG HEADING HERE</h4><p>Lorem ipsum is simply dummy text of the printing and typesetting industry. Lorem Ipsum has been the industry's.</p><span class="more">READ MORE</span></div></article>
    <article class="post"><div class="art" role="img" aria-label="Hexagon wood tabletop with epoxy" style="background:linear-gradient(135deg,#d9a85c,#3a86b4,#e1b67a)"></div><div class="body"><h4>BLOG HEADING HERE</h4><p>Lorem ipsum is simply dummy text of the printing and typesetting industry. Lorem Ipsum has been the industry's.</p><span class="more">READ MORE</span></div></article>
  </div>
</section>

<section class="abs features">
  <div class="feature"><svg viewBox="0 0 40 34"><path d="M2 6h22v18H2zM24 12h8l6 6v6H24"/><circle cx="10" cy="27" r="3"/><circle cx="31" cy="27" r="3"/></svg><b>FREE DELIVERY</b><span>On Select Orders</span></div>
  <div class="feature"><svg viewBox="0 0 40 34"><circle cx="20" cy="17" r="13"/><path d="M20 10v14M16 13h6a3 3 0 0 1 0 6h-4a3 3 0 0 0 0 6h6"/></svg><b>LOW PRICING</b><span>Competitive Industry Pricing</span></div>
  <div class="feature"><svg viewBox="0 0 40 34"><path d="M10 4h6l3 8-4 3a18 18 0 0 0 8 8l3-4 8 3v6a3 3 0 0 1-3 3C17 31 7 21 7 7a3 3 0 0 1 3-3z"/></svg><b>CALL TO ORDER</b><span>+1 (555) 010-2846</span></div>
  <div class="feature"><svg viewBox="0 0 40 34"><path d="M8 20v-4a12 12 0 0 1 24 0v4"/><rect x="5" y="18" width="6" height="10" rx="2"/><rect x="29" y="18" width="6" height="10" rx="2"/></svg><b>PHONE SUPPORT</b><span>8-5pm Support</span></div>
</section>

<div class="abs forest" role="img" aria-label="Silhouette of a pine forest fading into the footer"></div>

<footer class="abs footer">
  <div class="newsletter">
    <h2 class="display">Subscribe to Our Newsletter</h2>
    <p>Signup to be the first to receive product releases, news, coupons, and updates from the mill!</p>
  </div>
  <div class="signup"><span class="field">Enter your email</span><span class="go">SUBSCRIBE</span></div>

  <div class="foot-brand"><span class="brand-mark"></span><span class="brand-name">Timberpour</span></div>
  <div class="col" style="left:384px"><h5>USEFUL LINKS</h5><a>Products</a><a>Categories</a><a>About Us</a><a>Blog</a><a>Epoxy Training</a><a>Contact Us</a></div>
  <div class="col" style="left:624px"><h5>INFORMATION</h5><a>Shipping Info</a><a>Privacy Policy</a><a>Conditions of Use</a><a>Site Map</a><a>Contact Us</a></div>
  <div class="col" style="left:868px"><h5>CONTACT US</h5><a>⌖ 48 Millpond Road, Cedar Falls</a><a>✉ hello@timberpour.shop</a><a>✆ +1 (555) 010-2846</a><div class="social"><i></i><i></i><i></i><i></i></div></div>

  <p class="copyright">©Copyright 2023 | All Rights Reserved</p>
  <span class="to-top"><svg width="14" height="14" viewBox="0 0 24 24"><path d="M5 15l7-7 7 7" stroke="#fff" stroke-width="3" fill="none"/></svg></span>
</footer>

</body>
</html>
```